Stridewell Clinic (Podiatry and Physiotherapy) Clinical Brochure

You are producing a brochure that will sit in clinical/medical waiting rooms for our business Stridewell Clinic. A clinic that providers podiatry and physiotherapy services.

As you can see on our website www.stridewellclinic.example.nz we provide 6 different brands/services:
- Brightmoor Solutions
- Kestrelbay Solutions
- Varden Solutions
- Tolverstone Rehabilitation
- Ashgrove Solutions
- Merriwether Solutions

People will generally have found us through an ad e.g. search fungal nail treatment and end up straight on www.brightmoorsolutions.example.nz and therefore, each of the brands should be seen as being separate entities although part of the bigger brand Stridewell Clinic.

We are looking at a brochure (open to bi-fold, tri-fold etc.) that highlights all of our brands as well as the services that each of our brands provide which can be found on each of the websites listed above. We want this to be professional and informative yet simple and easy to read - this interpretation can be somewhat left up to you. This brochure will sit in waiting rooms/clinical environments.

I have attached our brand strategy so that you can understand our fonts and colours. I have also attached our logos for reference.

```html
<!DOCTYPE html>
<html lang="en">
<head>
<meta charset="utf-8">
<title>Stridewell Clinic – Clinical Brochure</title>
<link rel="stylesheet" href="https://fonts.googleapis.com/css2?family=Montserrat:wght@400;600;700;800&display=swap">
<style>
  :root {
    --blue: #1c6fd6;
    --blue-deep: #1457ad;
    --ink: #1c1d21;
    --paper: #ffffff;
    --backdrop: #e8e9ec;
    --photo-warm: #d9cfc6;
    --photo-cool: #b9c9dc;
    --muted: #5d6470;
  }
  * { box-sizing: border-box; margin: 0; padding: 0; }
  html, body { width: 857px; height: 1200px; overflow: hidden; }
  body { background: var(--backdrop); font-family: "Montserrat", sans-serif; color: var(--ink); }

  .spread {
    position: absolute; left: 20px; width: 817px; height: 575px;
    background: var(--paper); overflow: hidden;
    box-shadow: 0 4px 18px rgba(0,0,0,.12);
  }
  .spread--outer { top: 20px; }
  .spread--inner { top: 605px; display: grid; grid-template-columns: 1fr 1fr; }
  .fold { position: absolute; left: 408px; top: 0; width: 1px; height: 100%; background: rgba(0,0,0,.08); }

  /* Outer spread */
  .outer-shapes { position: absolute; inset: 0; }
  .photo-circle { position: absolute; border-radius: 50%; border: 6px solid var(--paper);
    background: radial-gradient(circle at 40% 40%, var(--photo-cool), #8fa6c4); }
  .photo-circle--warm { background: radial-gradient(circle at 40% 40%, #f1e4dc, var(--photo-warm)); }
  .back-url { position: absolute; left: 30px; bottom: 26px; font-size: 10px; font-weight: 600; color: var(--paper); letter-spacing: .3px; }
  .cover-photo { position: absolute; left: 409px; top: 0; width: 408px; height: 300px;
    background: linear-gradient(135deg, #e6ddd3 0%, #c8b8a8 45%, #9fb3c9 100%); }
  .cover-tagline { position: absolute; right: 28px; top: 392px; width: 250px; text-align: right;
    font-size: 14px; font-weight: 800; line-height: 1.3; color: var(--ink); text-transform: uppercase; }
  .brand { position: absolute; right: 28px; bottom: 34px; text-align: left; }
  .brand__name { font-size: 26px; font-weight: 800; color: var(--blue); line-height: 1; }
  .brand__sub { font-size: 10px; font-weight: 600; color: var(--muted); margin-top: 5px; }

  /* Inner spread */
  .panel { display: grid; grid-template-columns: 1fr 1fr; grid-template-rows: repeat(3, 1fr); gap: 8px; padding: 10px; }
  .photo { border-radius: 18px; background: linear-gradient(150deg, var(--photo-cool), #7f9cc0); }
  .photo--warm { background: linear-gradient(150deg, #efe2d8, var(--photo-warm)); }
  .service { border-radius: 48px 12px 48px 12px; padding: 22px 16px; color: var(--paper);
    display: flex; flex-direction: column; justify-content: center; min-width: 0; }
  .service--blue { background: var(--blue); }
  .service--dark { background: var(--ink); }
  .service__title { font-size: 17px; font-weight: 800; line-height: 1.15; }
  .service__text { font-size: 10.5px; font-weight: 400; line-height: 1.45; margin-top: 8px; opacity: .9; }
  .service__url { font-size: 7px; font-weight: 600; margin-top: 8px; opacity: .85; white-space: nowrap; letter-spacing: 0; }
</style>
</head>
<body>

<section class="spread spread--outer" aria-label="Brochure outside">
  <svg class="outer-shapes" width="817" height="575" viewBox="0 0 817 575" aria-hidden="true">
    <path d="M0 330 Q180 300 408 420 L408 575 L0 575 Z" fill="#1c6fd6"/>
    <path d="M409 300 L817 300 L817 320 L640 378 Z" fill="#1c6fd6"/>
    <path d="M409 300 L600 300 L540 340 Z" fill="#1457ad"/>
    <path d="M560 575 Q700 470 817 500 L817 575 Z" fill="#1c6fd6" opacity=".12"/>
  </svg>
  <div class="photo-circle" style="left:40px;top:30px;width:130px;height:130px" role="img" aria-label="Photo of a foot being examined"></div>
  <div class="photo-circle photo-circle--warm" style="left:200px;top:55px;width:120px;height:120px" role="img" aria-label="Photo of nail treatment"></div>
  <div class="photo-circle photo-circle--warm" style="left:95px;top:175px;width:115px;height:115px" role="img" aria-label="Photo of a heel support"></div>
  <div class="photo-circle" style="left:245px;top:205px;width:110px;height:110px" role="img" aria-label="Photo of ankle rehabilitation"></div>
  <p class="back-url">www.stridewellclinic.example.nz</p>

  <div class="cover-photo" role="img" aria-label="Photo of a smiling family together at home"></div>
  <p class="cover-tagline">Your feet carry you through life, so make sure you put the right foundation</p>
  <div class="brand">
    <p class="brand__name">Stridewell Clinic</p>
    <p class="brand__sub">Podiatry and Physiotherapy</p>
  </div>
  <div class="fold"></div>
</section>

<section class="spread spread--inner" aria-label="Brochure inside">
  <div class="panel">
    <article class="service service--blue">
      <h2 class="service__title">Brightmoor Solutions</h2>
      <p class="service__text">Gentle treatment for clear, healthy nails.</p>
      <p class="service__url">www.brightmoorsolutions.example.nz</p>
    </article>
    <div class="photo" role="img" aria-label="Photo of a gloved hand treating a toenail"></div>
    <div class="photo photo--warm" role="img" aria-label="Photo of a podiatrist examining a foot"></div>
    <article class="service service--dark">
      <h2 class="service__title">Kestrelbay Solutions</h2>
      <p class="service__text">Lasting relief from painful ingrown toenails.</p>
    </article>
    <article class="service service--blue">
      <h2 class="service__title">Varden Solutions</h2>
      <p class="service__text">Targeted care to ease heel pain.</p>
    </article>
    <div class="photo" role="img" aria-label="Photo of a heel being massaged"></div>
  </div>
  <div class="panel">
    <div class="photo photo--warm" role="img" aria-label="Photo of an ankle exercise with a band"></div>
    <article class="service service--blue">
      <h2 class="service__title">Tolverstone Rehabilitation</h2>
      <p class="service__text">Rebuild strength and movement after injury.</p>
    </article>
    <article class="service service--dark">
      <h2 class="service__title">Ashgrove Solutions</h2>
      <p class="service__text">Restore the look of damaged nails.</p>
    </article>
    <div class="photo" role="img" aria-label="Photo of painted, healthy toenails"></div>
    <div class="photo photo--warm" role="img" aria-label="Photo of a clinic treatment room"></div>
    <article class="service service--blue">
      <h2 class="service__title">Merriwether Solutions</h2>
      <p class="service__text">Everyday foot care for every age.</p>
    </article>
  </div>
  <div class="fold"></div>
</section>

</body>
</html>
```